Business card design needed for Automotive Reconditioning business

I have a logo design i just cant decide on the best color or layout for the business card, I will upload all the files so you can see all colors schemes we are considering. I have other file formats if needed let me know.

Target Market(s)

automotive dealerships

Contact Information for Business Card

HERE are the Descriptions and info needed on the card:
Interior Repair: Leather carpet burns panels dash Deoderize
Dealer products and Vin Verify
( spot for name and cell number) My name is Norman Bexley phone 614 352-4180 Title COO www.QuorvalMotive.com

Font styles to use
Sans Serif
Other font styles liked:
• what ever you think looks best

Requirements
Must have
• Must be able to change the name and phone for employees

```html
<!DOCTYPE html>
<html lang="en">
<head>
<meta charset="UTF-8">
<title>Quorval Motive – Business Cards</title>
<link href="https://fonts.googleapis.com/css2?family=Open+Sans:wght@400;600;700;800&display=swap" rel="stylesheet">
<style>
  :root {
    --backdrop: #161616;
    --card: #211f20;
    --card-edge: #2b292a;
    --accent: #8dc63f;
    --text-light: #e6e6e6;
    --text-muted: #bdbdbd;
    --rule: #4a4849;
  }
  * { box-sizing: border-box; margin: 0; padding: 0; }
  html, body {
    width: 1200px;
    height: 900px;
    overflow: hidden;
    background: var(--backdrop);
    font-family: "Open Sans", Arial, sans-serif;
  }
  .sheet {
    width: 1200px;
    height: 900px;
    display: flex;
    align-items: center;
    justify-content: center;
    gap: 60px;
  }
  .card {
    width: 520px;
    height: 320px;
    background: var(--card);
    border: 1px solid var(--card-edge);
    border-radius: 22px;
    display: flex;
    flex-direction: column;
    align-items: center;
    justify-content: center;
    text-align: center;
    padding: 30px;
  }
  .brand {
    display: flex;
    align-items: center;
    gap: 12px;
  }
  .brand-mark {
    width: 18px;
    height: 18px;
    background: var(--accent);
  }
  .brand-name {
    font-weight: 800;
    font-size: 34px;
    letter-spacing: 1px;
    color: var(--text-light);
    text-transform: uppercase;
  }
  .rule {
    width: 190px;
    height: 1px;
    background: var(--rule);
    margin: 14px 0;
  }
  .services-title {
    color: var(--accent);
    font-weight: 600;
    font-size: 15px;
  }
  .services-list {
    color: var(--text-muted);
    font-size: 14px;
    line-height: 1.4;
    max-width: 230px;
    margin-top: 2px;
  }
  .person-name {
    color: var(--accent);
    font-weight: 700;
    font-size: 22px;
    text-transform: uppercase;
    letter-spacing: 0.5px;
    margin-top: 18px;
  }
  .person-title {
    color: var(--text-muted);
    font-size: 14px;
  }
  .contact {
    font-size: 16px;
    color: var(--text-muted);
    line-height: 1.5;
  }
  .contact-label {
    color: var(--accent);
    font-weight: 600;
  }
</style>
</head>
<body>
  <main class="sheet">
    <section class="card card-back">
      <div class="brand">
        <span class="brand-mark"></span>
        <span class="brand-name">Quorval Motive</span>
      </div>
      <div class="rule"></div>
      <p class="services-title">Interior Repair:</p>
      <p class="services-list">Leather carpet burns panels dash Deoderize Dealer products and Vin Verify</p>
      <div class="rule"></div>
    </section>

    <section class="card card-front">
      <div class="brand">
        <span class="brand-mark"></span>
        <span class="brand-name">Quorval Motive</span>
      </div>
      <p class="person-name">Norman Bexley</p>
      <p class="person-title">CEO</p>
      <div class="rule"></div>
      <p class="contact"><span class="contact-label">P:</span> 614 352-4180</p>
      <p class="contact"><span class="contact-label">W:</span> www.QuorvalMotive.com</p>
    </section>
  </main>
</body>
</html>
```